Pastor's Lantern: How To Help Church Leaders Remain Strong In Their Callings.

I have created a 250-page book tentatively entitled, Pastor's Lantern, subtitle: A Handbook To Help Church Leaders Remain Strong in Their Callings. The chapters are taken from my podcast of the same name on Tunevo and website: pastorslantern.example which will need updating soon. The purpose of the book is to provide practical solutions to pastors/leaders about everyday issues faced in ministry such as loneliness, financial challenges, a pastor's family problems, sexual temptation ...etc. You can get an idea of the topics from Tunevo.
Updates

As mentioned in the brief, I am looking for something that will communicate solutions. My podcast, Pastor's Lantern from which this material originates is all about practical help for local pastors in facing the challenges of daily ministry. The logo I sent was designed for concept purposes only. It does not need to be on the cover necessarily unless it feeds into the overall theme.

Target Market(s)

Pastors and Church Leaders in the Christian Faith

Industry/Entity Type

Religious

Font styles to use
Serif

Colors

Designer to choose colors to be used in the design.

Requirements
Must have
• Crisp copy and lines. People see covers for 3 seconds. If they are not drawn in by complicated themes, I have failed. Many of the designs so far do not address the topic of the book in a way that impacts. This is about a toolbox or book that provides solutions to their everyday challenges. If it doesn't somehow point to tools, it should instead point to getting solutions.
Nice to have
• I have included a copy of my current logo. If you can incorporate it, fine. If you have a better idea, I am open to that and would be interested in contributing more if the logo is superior. The logo is not essential to either front or back cover..
Should not have
• Simplistic religious themes from often used pics. I will peruse other book covers in my genre. If I find the same pic used, it disqualifies the design immediately no matter how much I like it. Target audience is ministers. Simplistic cross designs have gotten less votes so far in polling. I want to grab attention with a compelling picture that communicates solutions.

```html
<!DOCTYPE html>
<html lang="en">
<head>
<meta charset="utf-8">
<title>Pastor's Lantern – Book Cover</title>
<link rel="stylesheet" href="https://fonts.googleapis.com/css2?family=Anton&family=Cinzel:wght@400;600&display=swap">
<style>
  :root {
    --backdrop: #2a2a2a;
    --sky-top: #cdb9a0;
    --sky-mid: #d99d6e;
    --haze: #c97b4f;
    --water-deep: #b9623f;
    --water-low: #c4846a;
    --water-bottom: #c9998a;
    --scene-dark: #7a3f28;
    --scene-glow: #e59a4e;
    --author: #3b3430;
    --kicker: #b8783a;
    --title: #f1ebe6;
    --subtitle: #fbefe4;
    --imprint: #ffffff;
  }
  * { margin: 0; padding: 0; box-sizing: border-box; }
  html, body {
    width: 1200px;
    height: 905px;
    overflow: hidden;
    background: var(--backdrop);
  }
  .canvas {
    width: 1200px;
    height: 905px;
    display: flex;
    align-items: center;
    justify-content: center;
  }
  .cover {
    position: relative;
    width: 540px;
    height: 845px;
    overflow: hidden;
  }
  .cover-sky {
    position: absolute;
    inset: 0;
    background:
      radial-gradient(ellipse 60% 25% at 85% 60%, rgba(236,160,80,0.55), rgba(236,160,80,0) 70%),
      linear-gradient(180deg,
        var(--sky-top) 0%,
        #d4ad88 22%,
        var(--sky-mid) 40%,
        var(--haze) 55%,
        var(--water-deep) 66%,
        var(--water-low) 82%,
        var(--water-bottom) 100%);
  }
  .boat-scene {
    position: absolute;
    left: 290px;
    top: 500px;
    width: 220px;
    height: 130px;
    border-radius: 6px;
    background:
      radial-gradient(ellipse 70% 45% at 50% 62%, rgba(122,63,40,0.75), rgba(122,63,40,0.25) 70%, rgba(122,63,40,0) 100%),
      linear-gradient(90deg, rgba(229,154,78,0) 0%, rgba(229,154,78,0.35) 100%);
  }
  .author {
    position: absolute;
    top: 50px;
    left: 0;
    right: 0;
    text-align: center;
    font-family: "Cinzel", serif;
    font-weight: 400;
    font-size: 31px;
    letter-spacing: 0.2em;
    color: var(--author);
  }
  .title { font-size: inherit; font-weight: normal; }
  .title-kicker {
    position: absolute;
    top: 180px;
    left: 0;
    right: 0;
    text-align: center;
    font-family: "Anton", sans-serif;
    font-size: 54px;
    letter-spacing: 0.46em;
    padding-left: 0.46em;
    color: var(--kicker);
    line-height: 1;
    text-shadow: 0 1px 2px rgba(80,40,15,0.35);
  }
  .title-main {
    position: absolute;
    top: 250px;
    left: 0;
    right: 0;
    text-align: center;
    font-family: "Anton", sans-serif;
    font-size: 128px;
    letter-spacing: 0.01em;
    color: var(--title);
    line-height: 1;
    text-shadow: 0 2px 4px rgba(90,40,20,0.35);
  }
  .subtitle {
    position: absolute;
    top: 408px;
    left: 0;
    right: 0;
    text-align: center;
    font-family: "Cinzel", serif;
    font-weight: 400;
    font-size: 20px;
    line-height: 1.1;
    color: var(--subtitle);
    letter-spacing: 0.02em;
    text-shadow: 0 1px 2px rgba(90,40,20,0.3);
  }
  .imprint {
    position: absolute;
    top: 782px;
    left: 0;
    right: 0;
    display: flex;
    align-items: center;
    justify-content: center;
    gap: 6px;
  }
  .imprint-mark {
    width: 12px;
    height: 12px;
    background: var(--imprint);
  }
  .imprint-name {
    font-family: "Cinzel", serif;
    font-weight: 600;
    font-size: 17px;
    color: var(--imprint);
    letter-spacing: 0.02em;
  }
</style>
</head>
<body>
  <main class="canvas">
    <section class="cover">
      <div class="cover-sky" role="img" aria-label="Misty orange sunrise sky over still water"></div>
      <div class="boat-scene" role="img" aria-label="Silhouette of a lone fisherman casting two rods from a small boat, reflected in calm water"></div>
      <p class="author">COREY M. SALVATO</p>
      <h1 class="title">
        <span class="title-kicker">PASTOR'S</span>
        <span class="title-main">LANTERN</span>
      </h1>
      <p class="subtitle">A HANDBOOK TO HELP CHURCH LEADERS<br>REMAIN STRONG IN THEIR CALLINGS</p>
      <div class="imprint">
        <span class="imprint-mark"></span>
        <span class="imprint-name">Pastor's Lantern</span>
      </div>
    </section>
  </main>
</body>
</html>
```